Landing page design for secure cloud backup web application

We would like a landing page design for our web application. Our app allows users to securely save their data in the cloud using their existing storage providers, such as tidLoft, Keg, Velmora Sky Locker, Pintaro stash and Quelvix Sole vault.
We make it extremely easy for individual users and small businesses to deploy sophisticated client-side encryption without having to worry about the technical complexity inherent in such solutions.
We already have the logo design done - I am attaching the logo file. We also have a preliminary website drafted at www.pemraq.test
I need a good color scheme, typography, layout, along with templates for 'help', 'about', 'privacy notice', 'legal' and such typical sub-pages
The design should be uncluttered, clean and minimalist

Target Market(s)

Individuals and medium/small businesses that are conscious about the security of their data in the cloud

Coding

Coded - Design and coding required

Number of Pages Required

4 page

Font styles to use
Sans Serif

Requirements
Must have
• Section where I describe the product along with pictures/images
• section for explainer video on main page
• FAQ section
• Help section
• Legal/privacynotice/terms of use section
• feedback section
Nice to have
• see existing draft site www.pemraq.test for content guidelines only.
• see attached logo files for color scheme guidelines - I am willing to accept change in the logo color if necessary to create a better web site look and feel
• Fonts on page should match font in the logo

```html
<!DOCTYPE html>
<html lang="en">
<head>
<meta charset="utf-8">
<title>Pemraq – Keep your data private</title>
<link href="https://fonts.googleapis.com/css2?family=Raleway:wght@400;500;600;700;800&display=swap" rel="stylesheet">
<style>
:root{
  --orange:#f7931e;
  --orange-dark:#e9851a;
  --ink:#2b2b2b;
  --text:#666;
  --muted:#888;
  --line:#e3e3e3;
  --white:#fff;
  --footer:#2e2e2e;
  --footer-bottom:#262626;
  --footer-text:#cfcfcf;
}
*{box-sizing:border-box;margin:0;padding:0}
html,body{width:1200px;height:2410px;overflow:hidden}
body{font-family:'Raleway',Arial,sans-serif;color:var(--ink);background:var(--white);position:relative}
.abs{position:absolute}

/* header */
.site-header{position:absolute;left:0;top:0;width:1200px;height:125px;background:var(--white)}
.brand{position:absolute;left:100px;top:38px;display:flex;align-items:center;gap:10px;font-size:34px;font-weight:800;color:#3a3a3a;letter-spacing:1px}
.brand-dot{width:26px;height:26px;border-radius:50%;background:var(--orange)}
.auth{position:absolute;right:100px;top:15px;display:flex;gap:10px}
.auth a{display:block;font-size:13px;font-weight:600;padding:9px 14px;text-decoration:none;letter-spacing:.5px}
.btn-login{background:#2f2f2f;color:var(--white);border:2px solid #555}
.btn-signup{background:var(--orange);color:var(--white)}
.main-nav{position:absolute;right:100px;top:74px;display:flex;gap:26px;align-items:center}
.main-nav a{font-size:12.5px;font-weight:600;color:#444;text-decoration:none;letter-spacing:.3px}
.main-nav a.active{background:var(--orange);color:var(--white);padding:7px 12px}
.search-icon{width:16px;height:16px}

/* hero */
.hero{position:absolute;left:0;top:125px;width:1200px;height:656px;background:#05070b}
.hero-art{position:absolute;left:145px;top:80px;width:910px;height:576px;background:radial-gradient(ellipse at 55% 45%,#4a86c9 0%,#1d4e86 30%,#0b1d33 60%,#05070b 85%)}
.hero-title{position:absolute;left:0;top:42px;width:1200px;text-align:center;color:var(--white);font-size:27px;font-weight:700;line-height:44px;letter-spacing:.3px}
.hero-arrow{position:absolute;top:310px;width:24px;height:36px}

/* intro */
.intro{position:absolute;left:0;top:781px;width:1200px;height:607px}
.intro h2{position:absolute;left:0;top:54px;width:1200px;text-align:center;font-size:25px;font-weight:700;color:#2d2d2d}
.intro p.lead{position:absolute;left:200px;top:112px;width:800px;text-align:center;font-size:12.5px;line-height:26px;color:var(--text)}
.provider{position:absolute;top:234px;width:240px}
.provider-thumb{width:240px;height:178px;border:4px solid #eee;box-shadow:0 1px 3px rgba(0,0,0,.15)}
.provider h3{margin-top:20px;font-size:14px;font-weight:700;color:#333;text-transform:uppercase}
.provider p{margin-top:12px;font-size:12px;line-height:22px;color:var(--muted);padding-right:12px}
.provider a{display:block;margin-top:10px;font-size:11px;font-weight:700;color:var(--orange);text-decoration:none}

/* features band */
.features{position:absolute;left:0;top:1388px;width:1200px;height:198px;background:var(--orange)}
.feature{position:absolute;top:26px;width:200px;text-align:center}
.feature svg{width:110px;height:110px;display:block;margin:0 auto}
.feature span{display:block;margin-top:10px;color:var(--white);font-size:14px;font-weight:700;letter-spacing:.3px}

/* faq / feedback / help */
.info{position:absolute;left:0;top:1586px;width:1200px;height:483px}
.info h2{font-size:25px;font-weight:700;color:#2d2d2d}
.faq{position:absolute;left:98px;top:45px;width:276px}
.faq-item{border-bottom:1px solid var(--line);padding:18px 0 16px}
.faq-item:first-of-type{padding-top:22px}
.faq-item h4{font-size:13.5px;font-weight:700;color:#333;line-height:22px;text-transform:uppercase}
.faq-item p{margin-top:8px;font-size:11.5px;color:var(--text)}
.faq .view-all{display:block;margin-top:22px;font-size:12px;font-weight:700;color:var(--orange)}
.feedback{position:absolute;left:415px;top:45px;width:380px}
.quote-box{position:relative;margin-top:35px;border:1px solid #ddd;padding:20px 18px 20px 48px;font-size:12px;line-height:28px;color:var(--text);box-shadow:0 1px 3px rgba(0,0,0,.08)}
.quote-box .q{position:absolute;color:var(--orange);font-weight:800;font-size:22px;line-height:1}
.quote-box:after{content:"";position:absolute;left:40px;bottom:-12px;width:20px;height:20px;background:var(--white);border-right:1px solid #ddd;border-bottom:1px solid #ddd;transform:rotate(45deg)}
.avatar{position:absolute;left:3px;top:222px;width:106px;height:106px;border-radius:50%;border:4px solid #eee;background:radial-gradient(circle at 50% 40%,#e0b48f,#8a5a3a)}
.reviewer{position:absolute;left:0;top:342px;width:112px;text-align:center;font-size:13.5px;font-weight:700;color:#333}
.help-box{position:absolute;left:829px;top:50px;width:272px;height:376px;overflow:hidden;background:linear-gradient(90deg,#8d8d8d 0%,#a6a6a6 55%,#cfcfcf 100%)}
.help-photo{position:absolute;left:150px;top:20px;width:122px;height:356px;background:linear-gradient(180deg,#d7cdc5 0%,#3a3a3a 45%,#1e1e1e 100%)}
.help-dot{position:absolute;left:30px;top:16px;width:30px;height:30px;border-radius:50%;background:#444}
.help-box h3{position:absolute;left:30px;top:70px;width:200px;font-size:31px;line-height:40px;font-weight:800;color:var(--white)}
.help-box p{position:absolute;left:30px;top:190px;width:140px;font-size:12px;line-height:24px;color:var(--white)}
.help-box a{position:absolute;left:33px;top:306px;width:140px;height:36px;line-height:32px;text-align:center;background:var(--orange);border:2px solid var(--white);color:var(--white);font-size:13.5px;font-weight:700;text-decoration:none}

/* footer */
.site-footer{position:absolute;left:0;top:2069px;width:1200px;height:252px;background:var(--footer)}
.f-col{position:absolute;top:34px}
.f-col h4{font-size:16px;font-weight:700;color:var(--white);text-transform:uppercase;margin-bottom:22px}
.f-divider{position:absolute;top:30px;width:1px;height:195px;background:#444}
.f-about p{font-size:12px;line-height:23px;color:var(--footer-text);width:220px}
.f-about .f-dot{display:block;width:28px;height:28px;border-radius:50%;background:#555;margin-bottom:6px}
.f-about strong{display:block;margin-top:6px;color:var(--white);font-size:12px}
.f-about a{color:var(--footer-text);font-size:12px}
.f-news p{font-size:12px;color:var(--footer-text)}
.f-news .field{margin-top:18px;width:245px;height:30px;background:#353535;border:1px solid #3c3c3c;color:#888;font-size:11.5px;padding:7px 10px}
.f-news .btn{display:inline-block;margin-top:16px;background:var(--orange);border:2px solid var(--white);color:var(--white);font-size:12.5px;font-weight:700;padding:7px 12px}
.social{display:flex;align-items:center;gap:18px;margin-bottom:14px;font-size:12px;color:var(--footer-text)}
.social i{display:block;width:36px;height:36px;border-radius:50%;background:#4a4a4a}
.contact-row{display:flex;gap:10px;font-size:12px;line-height:26px;color:var(--footer-text);margin-bottom:4px}
.contact-row svg{width:14px;height:14px;margin-top:5px;flex:none}
.footer-bottom{position:absolute;left:0;top:2321px;width:1200px;height:89px;background:var(--footer-bottom);text-align:center}
.footer-bottom nav{margin-top:30px;font-size:12px;color:var(--footer-text)}
.footer-bottom nav span{margin:0 8px}
.footer-bottom p{margin-top:10px;font-size:11.5px;color:var(--footer-text)}
</style>
</head>
<body>

<header class="site-header">
  <div class="brand"><span class="brand-dot"></span>Pemraq</div>
  <div class="auth"><a class="btn-login" href="#">LOG IN</a><a class="btn-signup" href="#">SIGN UP</a></div>
  <nav class="main-nav">
    <a class="active" href="#">HOME</a>
    <a href="#">ABOUT US</a>
    <a href="#">LEARN MORE/FAQ</a>
    <a href="#">DEVELOPER</a>
    <a href="#">CONTACT US</a>
    <svg class="search-icon" viewBox="0 0 16 16"><circle cx="6.5" cy="6.5" r="4.5" fill="none" stroke="#f7931e" stroke-width="2"/><line x1="10" y1="10" x2="14.5" y2="14.5" stroke="#f7931e" stroke-width="2.4" stroke-linecap="round"/></svg>
  </nav>
</header>

<section class="hero">
  <div class="hero-art" role="img" aria-label="Glowing globe with connected user icons above a tablet and a phone"></div>
  <h1 class="hero-title">PEMRAQ HAS A SIMPLE VISION. YOUR DATA BELONGS TO YOU AND NO<br>ONE ELSE.&nbsp; WE MAKE IT REALLY EASY TO KEEP IT THAT WAY.</h1>
  <svg class="hero-arrow" style="left:30px" viewBox="0 0 24 36"><polyline points="18,6 6,18 18,30" fill="none" stroke="#fff" stroke-width="3.5"/></svg>
  <svg class="hero-arrow" style="left:1146px" viewBox="0 0 24 36"><polyline points="6,6 18,18 6,30" fill="none" stroke="#fff" stroke-width="3.5"/></svg>
</section>

<section class="intro">
  <h2>KEEP YOUR DATA PRIVATE WITHOUT BREAKING A SWEAT</h2>
  <p class="lead">You have data you want to keep to yourself. You want it safe in the cloud so you can get at it anywhere. You don't want to mess with encryption keys yet you want to keep hackers and snoops out. You know it shouldn't be so hard.<br>You're right.</p>

  <article class="provider" style="left:97px">
    <div class="provider-thumb" role="img" aria-label="Rows of metal safe deposit boxes" style="background:linear-gradient(135deg,#6d6d6d,#2e2e2e)"></div>
    <h3>tidLoft</h3>
    <p>Sed ut perspiciatis unde omnis iste natus error sit voluptatem doloremque lau dantiumidicta sunt explicabo.</p>
    <a href="#">READ MORE &gt;&gt;</a>
  </article>
  <article class="provider" style="left:354px">
    <div class="provider-thumb" role="img" aria-label="Server room corridor" style="background:linear-gradient(180deg,#9aa3ab,#2a2f35 50%,#c9ccd0)"></div>
    <h3>Keg</h3>
    <p>Sed ut perspiciatis unde omnis iste natus error sit voluptatem doloremque lau dantiumidicta sunt explicabo.</p>
    <a href="#">READ MORE &gt;&gt;</a>
  </article>
  <article class="provider" style="left:611px">
    <div class="provider-thumb" role="img" aria-label="Blue cloud with network cables" style="background:linear-gradient(135deg,#1b2a4a,#3f7fcf 60%,#0e1a30)"></div>
    <h3>Velmora Sky Locker</h3>
    <p>Sed ut perspiciatis unde omnis iste natus error sit voluptatem doloremque lau dantiumidicta sunt explicabo.</p>
    <a href="#">READ MORE &gt;&gt;</a>
  </article>
  <article class="provider" style="left:868px">
    <div class="provider-thumb" role="img" aria-label="Colourful app icons on a tablet screen" style="background:linear-gradient(135deg,#f6b233,#e7536b 40%,#5cc2e8 75%,#8fd26a)"></div>
    <h3>Pintaro &amp; Quelvix vault</h3>
    <p>Sed ut perspiciatis unde omnis iste natus error sit voluptatem doloremque lau dantiumidicta sunt explicabo.</p>
    <a href="#">READ MORE &gt;&gt;</a>
  </article>
</section>

<section class="features">
  <div class="feature" style="left:104px">
    <svg viewBox="0 0 110 110"><polygon points="32,6 78,6 104,55 78,104 32,104 6,55" fill="none" stroke="#fff" stroke-width="3"/><polygon points="37,15 73,15 94,55 73,95 37,95 16,55" fill="none" stroke="#fff" stroke-width="2"/><path d="M38 66h34a9 9 0 0 0 0-18 13 13 0 0 0-25-3 10 10 0 0 0-9 21z" fill="#fff"/></svg>
    <span>USE YOUR CLOUD</span>
  </div>
  <div class="feature" style="left:304px">
    <svg viewBox="0 0 110 110"><polygon points="32,6 78,6 104,55 78,104 32,104 6,55" fill="none" stroke="#fff" stroke-width="3"/><polygon points="37,15 73,15 94,55 73,95 37,95 16,55" fill="none" stroke="#fff" stroke-width="2"/><path d="M55 36a12 12 0 0 0-12 12c0 10 12 24 12 24s12-14 12-24a12 12 0 0 0-12-12z" fill="#fff"/><circle cx="55" cy="48" r="4.5" fill="#f7931e"/></svg>
    <span>ACCESS ANYWHERE</span>
  </div>
  <div class="feature" style="left:500px">
    <svg viewBox="0 0 110 110"><polygon points="32,6 78,6 104,55 78,104 32,104 6,55" fill="none" stroke="#fff" stroke-width="3"/><polygon points="37,15 73,15 94,55 73,95 37,95 16,55" fill="none" stroke="#fff" stroke-width="2"/><rect x="38" y="42" width="28" height="28" rx="3" fill="none" stroke="#fff" stroke-width="3"/><path d="M50 60l3-8 16-16 5 5-16 16z" fill="#fff"/></svg>
    <span>EASY TO USE</span>
  </div>
  <div class="feature" style="left:697px">
    <svg viewBox="0 0 110 110"><polygon points="32,6 78,6 104,55 78,104 32,104 6,55" fill="none" stroke="#fff" stroke-width="3"/><polygon points="37,15 73,15 94,55 73,95 37,95 16,55" fill="none" stroke="#fff" stroke-width="2"/><path d="M55 36l19 33H36z" fill="#fff"/><rect x="53" y="47" width="4" height="12" fill="#f7931e"/><rect x="53" y="62" width="4" height="4" fill="#f7931e"/></svg>
    <span>ZERO KNOWLEDGE</span>
  </div>
  <div class="feature" style="left:902px">
    <svg viewBox="0 0 110 110"><polygon points="32,6 78,6 104,55 78,104 32,104 6,55" fill="none" stroke="#fff" stroke-width="3"/><polygon points="37,15 73,15 94,55 73,95 37,95 16,55" fill="none" stroke="#fff" stroke-width="2"/><rect x="36" y="42" width="30" height="22" fill="none" stroke="#fff" stroke-width="3"/><rect x="44" y="48" width="30" height="22" fill="#f7931e" stroke="#fff" stroke-width="3"/><polyline points="47,67 56,58 62,64 66,60 72,67" fill="none" stroke="#fff" stroke-width="2"/></svg>
    <span>MULTIPLE APPS</span>
  </div>
</section>

<section class="info">
  <div class="faq">
    <h2>FAQ</h2>
    <div class="faq-item"><h4>Where is my data stored?</h4><p>Your data is stored on your accounts ..</p></div>
    <div class="faq-item"><h4>So what does it cost?</h4><p style="line-height:20px">We are currently rolling out a private beta. we do plan to start charging ..</p></div>
    <div class="faq-item"><h4>How do you ensure that no one else can see my data?</h4><p>We use the latest in-browser AES-256 bit ..</p></div>
    <a class="view-all" href="#">VIEW ALL</a>
  </div>

  <div class="feedback">
    <h2>FEEDBACK</h2>
    <blockquote class="quote-box">
      <span class="q" style="left:16px;top:22px">&ldquo;</span>
      Sed ut perspiciatis unde omnis iste natus error sit voluptatem accusantium doloremque laudantium, totam rem aperiam, eaque ipsa quae ab illo inventore veritatis
      <span class="q" style="right:40px;bottom:10px">&rdquo;</span>
    </blockquote>
    <div class="avatar" role="img" aria-label="Portrait photo of the customer"></div>
    <div class="reviewer">Lena Marsh</div>
  </div>

  <aside class="help-box">
    <div class="help-photo" role="img" aria-label="Support agent wearing a headset"></div>
    <span class="help-dot"></span>
    <h3>DO YOU NEED ANY HELP</h3>
    <p>Lorem ipsum dolor sit amet, consectetur adipiscing elit, sed do eiusmod</p>
    <a href="#">CLICK HERE</a>
  </aside>
</section>

<footer class="site-footer">
  <div class="f-col f-about" style="left:100px">
    <h4>About Us</h4>
    <span class="f-dot"></span>
    <p>Pemraq is based out of Harlow Vale, NR. We are a team of developers with a passion for building truly useful web applications..</p>
    <strong>Drop us a note at :</strong>
    <a href="#">feedback@pemraq.test</a>
  </div>
  <span class="f-divider" style="left:360px"></span>
  <div class="f-col f-news" style="left:389px">
    <h4>Newsletter</h4>
    <p>Register Your Email Id to Get Our News</p>
    <div class="field">Email Address</div>
    <span class="btn">SIGN IN</span>
  </div>
  <span class="f-divider" style="left:662px"></span>
  <div class="f-col" style="left:698px">
    <h4>Follow Us On</h4>
    <div class="social"><i></i>Linkhall</div>
    <div class="social"><i></i>Chirpa</div>
    <div class="social"><i></i>Ringlo</div>
  </div>
  <span class="f-divider" style="left:838px"></span>
  <div class="f-col" style="left:862px">
    <h4>Contact Us</h4>
    <div class="contact-row"><svg viewBox="0 0 14 14"><path d="M7 1a4.5 4.5 0 0 0-4.5 4.5C2.5 9 7 13 7 13s4.5-4 4.5-7.5A4.5 4.5 0 0 0 7 1z" fill="#f7931e"/></svg><span>Reg. Office: 4, Elm Row, 2210 Lane,<br>Dunmere</span></div>
    <div class="contact-row"><svg viewBox="0 0 14 14"><rect x="1" y="3" width="12" height="9" fill="#f7931e"/><polyline points="1,3 7,8 13,3" fill="none" stroke="#2e2e2e" stroke-width="1.2"/></svg><span>hello@pemraq.test</span></div>
    <div class="contact-row"><svg viewBox="0 0 14 14"><path d="M3 1l3 3-1.5 2a8 8 0 0 0 3.5 3.5L10 8l3 3-2 2C6 13 1 8 1 3z" fill="#f7931e"/></svg><span>+100 5550 0199</span></div>
  </div>
</footer>

<div class="footer-bottom">
  <nav>Legal<span>|</span>Terms and Use<span>|</span>Privacy Policy</nav>
  <p>Copyrights © 2015 Pemraq. All rights are reserved.</p>
</div>

</body>
</html>
```